Medical Clinic Group Looking for Website Design

We own and operate medical clinics and are looking looking to revamp our website. Our current website is www.brightharborcare.ca We need our website to be more functional, user friendly, and easier to maintain.

```html
<!DOCTYPE html>
<html lang="en">
<head>
<meta charset="utf-8">
<title>Bright Harbor Care</title>
<link href="https://fonts.googleapis.com/css2?family=Red+Hat+Display:wght@300;400;500;700&display=swap" rel="stylesheet">
<style>
:root{
  --cyan:#17c9d6;
  --ink:#2b2b33;
  --muted:#5a5a66;
  --navy:#0b0c3a;
  --band:#e4f7fa;
  --white:#ffffff;
}
*{margin:0;padding:0;box-sizing:border-box}
html,body{width:801px;height:1200px;overflow:hidden;background:var(--white)}
body{position:relative;font-family:"Red Hat Display",Arial,sans-serif;color:var(--ink)}
.abs{position:absolute}
.hero-photo{left:0;top:0;width:801px;height:400px;
  background:linear-gradient(100deg,#dcf8fa 0%,#e3f6f8 30%,#d9e6ea 45%,#b7bec4 62%,#c9ced2 80%,#e1e4e6 100%)}
.hero-wave{left:0;top:0}
.brand{display:flex;align-items:center;gap:7px;color:var(--cyan);font-weight:400;white-space:nowrap}
.brand-dot{width:18px;height:18px;border-radius:50%;border:2px solid var(--cyan)}
.site-brand{left:112px;top:18px;font-size:15px}
.nav{left:333px;top:21px;display:flex;font-size:7px;color:#1a1a22}
.nav a{color:inherit;text-decoration:none;margin-right:24px}
.nav a.active{color:var(--cyan);text-decoration:underline;font-weight:500}
.book-btn{left:616px;top:16px;width:75px;height:20px;border:1px solid #222;border-radius:11px;font-size:7.5px;display:flex;align-items:center;justify-content:center;font-weight:500}
.hero-tag{left:112px;top:119px;border-left:1px solid #7a8a90;padding-left:7px;font-size:8.5px;color:var(--cyan);line-height:17px}
.hero-title{left:111px;top:138px;font-size:28px;font-weight:400;line-height:33px;color:var(--ink);letter-spacing:-.3px}
.hero-title .accent{display:block;color:var(--cyan);font-weight:700;font-size:26.5px}
.hero-copy{left:112px;top:211px;width:245px;font-size:9px;line-height:14px;color:#2e2e36}
.btn{background:var(--cyan);color:var(--white);font-weight:700;border-radius:14px;display:flex;align-items:center;justify-content:center}
.hero-btn{left:113px;top:270px;width:126px;height:23px;font-size:8px}
.about-photo{left:112px;top:420px;width:242px;height:242px;border-radius:50%;
  background:radial-gradient(circle at 50% 40%,#f6eeea 0%,#e6dcd6 45%,#c7cdd3 75%,#aeb9c2 100%)}
.about-kicker{left:391px;top:421px;font-size:12.5px;color:var(--cyan)}
.about-title{left:391px;top:436px;font-size:25px;font-weight:500;color:var(--ink)}
.about-copy{left:391px;top:474px;width:285px;font-size:8.7px;line-height:14.6px;color:var(--muted);font-weight:300}
.about-copy b{font-weight:500;color:var(--ink)}
.about-copy p+p{margin-top:14.6px}
.about-btn{left:391px;top:634px;width:101px;height:25px;font-size:8.3px}
.band{left:0;top:717px;width:801px;height:300px;background:var(--band)}
.feature{top:770px;width:180px;text-align:center}
.feature svg{display:block;margin:0 auto}
.feature h3{font-weight:400;font-size:15px;color:var(--ink);margin-top:14px}
.footer-wave{left:0;top:880px}
.footer-brand{left:65px;top:1002px;font-size:16px}
.footer-note{left:65px;top:1041px;width:165px;font-size:7.3px;line-height:14.5px;color:#b9bad0;font-weight:300}
.foot-head{top:997px;font-size:9.5px;font-weight:700;color:var(--white)}
.quick{left:257px;top:1028px;font-size:7.5px;color:#d4d5e4;line-height:21px}
.contact{left:383px;top:1030px;font-size:9px;color:#d4d5e4;line-height:11.5px}
.contact p{margin-bottom:9px}
.subscribe{left:556px;top:1031px;font-size:7.5px;color:#d4d5e4}
.email-field{left:556px;top:1058px;width:179px;height:32px;background:var(--white);border-radius:16px;font-size:6px;color:#9a9aa5;padding-left:11px;display:flex;align-items:center}
.email-go{position:absolute;right:10px;top:6px;width:21px;height:21px;border-radius:50%;background:var(--cyan)}
.rule{left:65px;top:1171px;width:668px;height:1px;background:#2a2b57}
.copyright{left:65px;top:1180px;font-size:9px;color:var(--white)}
.copyright span{color:var(--cyan)}
.social{left:651px;top:1178px;display:flex;gap:12px}
.social i{display:block;width:11px;height:11px;border-radius:50%;background:#7f8fb0}
</style>
</head>
<body>
  <div class="abs hero-photo" role="img" aria-label="Physiotherapist guiding a patient through a resistance band exercise in a bright clinic room"></div>
  <svg class="abs hero-wave" width="801" height="400" viewBox="0 0 801 400">
    <path d="M0,342 C100,362 250,372 330,362 C400,350 430,325 480,332 C540,340 560,385 620,378 C680,372 730,320 801,305 L801,400 L0,400 Z" fill="#ffffff"/>
  </svg>

  <div class="abs brand site-brand"><span class="brand-dot"></span>Bright Harbor Care</div>
  <nav class="abs nav">
    <a class="active">Home</a><a>Locations</a><a>For Patients</a><a>For Providers</a><a>About Us</a>
  </nav>
  <div class="abs book-btn">Book Online</div>

  <div class="abs hero-tag">Sports Medicine services</div>
  <h1 class="abs hero-title">Now Available At<span class="accent">Our Harbourview Location</span></h1>
  <p class="abs hero-copy">Bright Harbor Care is continually adding and improving our services to provide&nbsp; patients with access to comprehensive care under one roof.</p>
  <div class="abs btn hero-btn">Download Referral Form</div>

  <div class="abs about-photo" role="img" aria-label="Woman raising her arms in celebration facing a city skyline"></div>
  <div class="abs about-kicker">About Us</div>
  <h2 class="abs about-title">Your Future Awaits</h2>
  <div class="abs about-copy">
    <p>At Bright Harbor Care, <b>work/life balance is at the core</b> of our culture. Our philosophy is simple: we take exceptional care of our people so that they can take exceptional care of our patients. Contact us to find out why so many <b>healthcare providers and medical professionals</b> have chosen to join our team.</p>
    <p>Bright <b>Harbor Care is currently looking for a full-time family physician</b> to join our growing team as we expand our operations. Cedar Valley is located in the heart of the <b>Silver Basin and is surrounded</b> by beautiful lakes, mountains, pristine vineyards and orchards.</p>
  </div>
  <div class="abs btn about-btn">More About Us</div>

  <div class="abs band"></div>

  <div class="abs feature" style="left:70px">
    <svg width="60" height="56" viewBox="0 0 60 56"><path d="M30,2 L57,28 L30,54 L3,28 Z" fill="none" stroke="#17c9d6" stroke-width="2" stroke-linejoin="round"/><circle cx="30" cy="21" r="5" fill="none" stroke="#17c9d6" stroke-width="1.6"/><path d="M21,37 v-4 a6,6 0 0 1 6,-6 h6 a6,6 0 0 1 6,6 v4 Z" fill="none" stroke="#17c9d6" stroke-width="1.6"/></svg>
    <h3>Find a Provider</h3>
  </div>
  <div class="abs feature" style="left:219px">
    <svg width="60" height="56" viewBox="0 0 60 56"><path d="M30,2 L57,28 L30,54 L3,28 Z" fill="none" stroke="#17c9d6" stroke-width="2" stroke-linejoin="round"/><path d="M22,18 l5,-3 l4,6 l-3,2 q2,5 6,7 l2,-3 l6,4 l-3,5 q-12,-2 -17,-18 Z" fill="none" stroke="#17c9d6" stroke-width="1.5" stroke-linejoin="round"/><circle cx="25" cy="33" r="4" fill="none" stroke="#17c9d6" stroke-width="1.5"/></svg>
    <h3>Services</h3>
  </div>
  <div class="abs feature" style="left:392px">
    <svg width="60" height="56" viewBox="0 0 60 56"><path d="M30,2 L57,28 L30,54 L3,28 Z" fill="none" stroke="#17c9d6" stroke-width="2" stroke-linejoin="round"/><rect x="19" y="17" width="22" height="20" rx="2" fill="none" stroke="#17c9d6" stroke-width="1.5"/><line x1="19" y1="22" x2="41" y2="22" stroke="#17c9d6" stroke-width="1.5"/><g fill="#17c9d6"><circle cx="24" cy="26" r="1.2"/><circle cx="28" cy="26" r="1.2"/><circle cx="32" cy="26" r="1.2"/><circle cx="36" cy="26" r="1.2"/><circle cx="24" cy="30" r="1.2"/><circle cx="28" cy="30" r="1.2"/><circle cx="32" cy="30" r="1.2"/><circle cx="36" cy="30" r="1.2"/></g></svg>
    <h3>Book an Appointment</h3>
  </div>
  <div class="abs feature" style="left:566px">
    <svg width="60" height="56" viewBox="0 0 60 56"><path d="M30,2 L57,28 L30,54 L3,28 Z" fill="none" stroke="#17c9d6" stroke-width="2" stroke-linejoin="round"/><path d="M30,36 q-8,-8 -8,-13 a8,8 0 0 1 16,0 q0,5 -8,13 Z" fill="none" stroke="#17c9d6" stroke-width="1.6"/><circle cx="30" cy="23" r="3" fill="none" stroke="#17c9d6" stroke-width="1.5"/><ellipse cx="30" cy="37" rx="9" ry="2.5" fill="none" stroke="#17c9d6" stroke-width="1.3"/></svg>
    <h3>Locations</h3>
  </div>

  <svg class="abs footer-wave" width="801" height="320" viewBox="0 880 801 320">
    <path d="M0,986 C60,975 90,920 148,909 C220,895 290,960 358,960 C430,960 480,920 562,922 C660,924 740,935 801,948 L801,1200 L0,1200 Z" fill="#0b0c3a"/>
  </svg>

  <div class="abs brand footer-brand"><span class="brand-dot"></span>Bright Harbor Care</div>
  <p class="abs footer-note">Please do not send medical questions to this email. If you have a medical question, contact your doctor's office directly. Visit our locations page or click here to find contact information for each of our locations.</p>

  <div class="abs foot-head" style="left:257px">Quick Links</div>
  <div class="abs quick">Home<br>Locations<br>For Patients<br>For Providers<br>About Us</div>

  <div class="abs foot-head" style="left:383px">Contact Us</div>
  <div class="abs contact">
    <p>2470 Maple Ridge Rd, Cedar Valley,<br>BC V0X 2K4, Canada</p>
    <p>Call us: 778.555.0142</p>
    <p>hello@brightharborcare.ca</p>
  </div>

  <div class="abs foot-head" style="left:556px">Stay connected</div>
  <div class="abs subscribe">Subscribe to get latest news from us</div>
  <div class="abs email-field">Email address
    <span class="email-go"><svg width="21" height="21" viewBox="0 0 21 21"><path d="M6,10.5 h9 M11,6.5 l4,4 l-4,4" fill="none" stroke="#fff" stroke-width="1.8" stroke-linecap="round" stroke-linejoin="round"/></svg></span>
  </div>

  <div class="abs rule"></div>
  <div class="abs copyright">©2022 by <span>Bright Harbor Care.</span> Proudly created with SiteForge.com</div>
  <div class="abs social"><i></i><i></i><i></i><i></i></div>
</body>
</html>
```